Powerpoint contest

We need to re-design our powerpoints to be much more consistent. All the details are mentioned here. I have more than 30 slides to be created in all.

https://www.pagewell.io/brivane/All-Powerpoints-3c81d27e90ab4f51a6c2e04b7d9f1a25

Requirements
Must have
• Colors should be greyscale and kvelcom pink (ea0a8e) used in small amounts just for accents.

```html
<!DOCTYPE html>
<html lang="en">
<head>
<meta charset="utf-8">
<title>Brivane – Company Metrics</title>
<link href="https://fonts.googleapis.com/css2?family=Arimo:wght@400;700&family=Open+Sans:wght@400;600;700&family=Oswald:wght@300;400&display=swap" rel="stylesheet">
<style>
  :root {
    --accent-pink: #ea0a8e;
    --ink: #111111;
    --bg: #ffffff;
    --grey-text: #7a7a7a;
    --grey-light: #d4d4d4;
    --grey-mid: #a9a9a9;
    --grey-dark: #7f7f7f;
  }
  html, body {
    margin: 0;
    padding: 0;
    overflow: hidden;
    background: var(--bg);
  }
  .slide {
    position: relative;
    width: 1200px;
    height: 673px;
    overflow: hidden;
    background: var(--bg);
  }
  .brand {
    position: absolute;
    top: 30px;
    left: 968px;
    display: flex;
    align-items: center;
    gap: 10px;
    font-family: "Arimo", sans-serif;
    font-weight: 700;
    font-size: 27px;
    color: var(--ink);
  }
  .brand-dot {
    width: 22px;
    height: 22px;
    border-radius: 50%;
    background: var(--accent-pink);
  }
  .metrics-title {
    position: absolute;
    top: 190px;
    left: 137px;
    margin: 0;
    font-family: "Arimo", sans-serif;
    font-weight: 700;
    font-size: 31px;
    color: var(--accent-pink);
    letter-spacing: 0.2px;
  }
  .metrics-list {
    position: absolute;
    top: 241px;
    left: 118px;
    width: 480px;
    margin: 0;
    padding: 0;
    list-style: none;
    font-family: "Arimo", sans-serif;
    font-weight: 700;
    font-size: 18.5px;
    line-height: 23px;
    color: var(--ink);
  }
  .metrics-list li {
    position: relative;
    padding-left: 30px;
    margin-bottom: 26px;
  }
  .metrics-list li::before {
    content: "";
    position: absolute;
    left: 2px;
    top: 9px;
    width: 7px;
    height: 7px;
    border: 1.3px solid var(--ink);
    border-radius: 50%;
  }
  .team-graphic {
    position: absolute;
    left: 0;
    top: 0;
  }
  .hub-title { font-family: "Open Sans", sans-serif; font-weight: 700; font-size: 19px; fill: var(--grey-text); }
  .hub-body { font-family: "Open Sans", sans-serif; font-size: 11px; fill: var(--grey-text); }
  .hub-body .strong { font-weight: 700; fill: #555; }
  .year-label { font-family: "Open Sans", sans-serif; font-size: 12.5px; fill: #fff; }
  .year-value { font-family: "Oswald", sans-serif; font-weight: 300; font-size: 28px; fill: #fff; }
</style>
</head>
<body>
<main class="slide">
  <div class="brand"><span class="brand-dot"></span>Brivane</div>

  <h1 class="metrics-title">COMPANY METRICS</h1>
  <ul class="metrics-list">
    <li>FOUNDED IN 2014 BY AN EX NIMBUSLY EMPLOYEE.</li>
    <li>HEADQUARTERED IN SAN RAMON, CA.</li>
    <li>TWO DEVELOPMENT CENTERS IN EASTERN EUROPE AND INDIA.</li>
    <li>THREE SUPPORT CENTERS IN EASTERN EUROPE AND INDIA.</li>
  </ul>

  <svg class="team-graphic" width="1200" height="673" viewBox="0 0 1200 673" aria-label="Team strength growth 2018 to 2020">
    <defs>
      <radialGradient id="hubFill" cx="45%" cy="35%" r="70%">
        <stop offset="0" stop-color="#ffffff"/>
        <stop offset="0.75" stop-color="#f6f6f6"/>
        <stop offset="1" stop-color="#e2e2e2"/>
      </radialGradient>
      <radialGradient id="ringFill" cx="50%" cy="40%" r="60%">
        <stop offset="0" stop-color="#ffffff"/>
        <stop offset="1" stop-color="#dcdcdc"/>
      </radialGradient>
      <linearGradient id="node2018" x1="0" y1="0" x2="0" y2="1">
        <stop offset="0" stop-color="#dcdcdc"/>
        <stop offset="1" stop-color="#b3b3b3"/>
      </linearGradient>
      <linearGradient id="node2019" x1="0" y1="0" x2="0" y2="1">
        <stop offset="0" stop-color="#c4c4c4"/>
        <stop offset="1" stop-color="#999999"/>
      </linearGradient>
      <linearGradient id="node2020" x1="0" y1="0" x2="0" y2="1">
        <stop offset="0" stop-color="#a6a6a6"/>
        <stop offset="1" stop-color="#7a7a7a"/>
      </linearGradient>
      <linearGradient id="band2018" x1="0" y1="1" x2="1" y2="0">
        <stop offset="0" stop-color="#e8e8e8"/>
        <stop offset="1" stop-color="#bdbdbd"/>
      </linearGradient>
      <linearGradient id="band2019" x1="0" y1="0" x2="1" y2="0">
        <stop offset="0" stop-color="#e6e6e6"/>
        <stop offset="1" stop-color="#a5a5a5"/>
      </linearGradient>
      <linearGradient id="band2020" x1="0" y1="0" x2="1" y2="1">
        <stop offset="0" stop-color="#bfbfbf"/>
        <stop offset="1" stop-color="#707070"/>
      </linearGradient>
      <filter id="softShadow" x="-30%" y="-30%" width="160%" height="160%">
        <feDropShadow dx="0" dy="3" stdDeviation="5" flood-color="#000" flood-opacity="0.25"/>
      </filter>
    </defs>

    <!-- connector bands -->
    <path d="M 790 255 Q 880 215 935 150 L 975 205 Q 900 260 830 300 Z" fill="url(#band2018)"/>
    <path d="M 840 320 Q 930 318 985 322 L 985 385 Q 930 378 840 380 Z" fill="url(#band2019)"/>
    <path d="M 820 400 Q 890 430 935 490 L 980 465 Q 900 390 840 345 Z" fill="url(#band2020)"/>

    <!-- segmented arc -->
    <path d="M 686.5 225 A 149 149 0 0 0 632 296" fill="none" stroke="#dcdcdc" stroke-width="27"/>
    <path d="M 630.3 301 A 149 149 0 0 0 630.3 393" fill="none" stroke="#b5b5b5" stroke-width="27"/>
    <path d="M 632 398 A 149 149 0 0 0 686.5 469" fill="none" stroke="#8c8c8c" stroke-width="27"/>

    <!-- hub -->
    <circle cx="772" cy="347" r="106" fill="url(#hubFill)" filter="url(#softShadow)"/>
    <text class="hub-title" x="775" y="304" text-anchor="middle">TEAM STRENGTH</text>
    <text class="hub-body" text-anchor="middle">
      <tspan x="777" y="356">OUR TEAM HAS INCREASED</tspan>
      <tspan x="777" y="376"><tspan class="strong">361%</tspan> IN THE PAST 3 YEARS. WE</tspan>
      <tspan x="777" y="396">ARE NOW OVER 76 MEMBERS</tspan>
      <tspan x="777" y="417">STRONG. WITH 43% WOMEN</tspan>
      <tspan x="777" y="437">AND 45% OTHER MINORITIES</tspan>
    </text>

    <!-- year nodes -->
    <g class="node">
      <circle cx="968" cy="169" r="60" fill="url(#ringFill)" filter="url(#softShadow)"/>
      <circle cx="968" cy="169" r="49" fill="url(#node2018)"/>
      <text class="year-label" x="968" y="168" text-anchor="middle">21 MEMBERS</text>
      <text class="year-value" x="968" y="201" text-anchor="middle">2018</text>
    </g>
    <g class="node">
      <circle cx="1020" cy="353" r="57" fill="url(#ringFill)" filter="url(#softShadow)"/>
      <circle cx="1020" cy="353" r="46" fill="url(#node2019)"/>
      <text class="year-label" x="1020" y="349" text-anchor="middle">59 MEMBERS</text>
      <text class="year-value" x="1020" y="382" text-anchor="middle">2019</text>
    </g>
    <g class="node">
      <circle cx="967" cy="529" r="60" fill="url(#ringFill)" filter="url(#softShadow)"/>
      <circle cx="967" cy="529" r="49" fill="url(#node2020)"/>
      <text class="year-label" x="967" y="527" text-anchor="middle">76 MEMBERS</text>
      <text class="year-value" x="967" y="560" text-anchor="middle">2020</text>
    </g>
  </svg>
</main>
</body>
</html>
```